Corvelles Concept Stationery design

With my provided logo I need stationery design for business cards, envelope (#10), letterhead, fax sheet, memo sheet and 9'' x 12'' presentation folder. I would aIso need an email signature design included. PMS COLORS are : Pantone 541C et 299C. Looking for a bold look, minimalist yet eye-catching look.

```html
<!DOCTYPE html>
<html lang="en">
<head>
<meta charset="utf-8">
<title>Corvelles Concept Stationery</title>
<link href="https://fonts.googleapis.com/css2?family=Inter:wght@400;600;700&display=swap" rel="stylesheet">
<style>
:root{
  --navy:#0d3a63;
  --sky:#1b9ad6;
  --ink:#2a2a2a;
  --rule:#8a8a8a;
  --paper:#ffffff;
  --backdrop:#d4d4d8;
  --cell:#f2f2f2;
}
*{box-sizing:border-box;margin:0;padding:0}
html,body{width:1200px;height:806px;overflow:hidden}
body{background:var(--backdrop);font-family:"Inter",Arial,sans-serif;color:var(--ink);position:relative}
.sheet{position:absolute;top:81px;width:497px;height:644px;background:var(--paper);border-top:6px solid var(--navy)}
.letterhead{left:89px}
.fax-sheet{left:614px}
.brand{position:absolute;left:50px;top:46px;display:flex;align-items:center;gap:6px}
.brand-dot{width:7px;height:7px;border-radius:50%;background:var(--sky)}
.brand-name{font-weight:700;font-size:13px;color:var(--ink);letter-spacing:.2px}
.contact{position:absolute;left:361px;top:35px;font-size:6.2px;line-height:9.4px;color:#333}
.contact .gap{height:6px}
.contact-line{display:flex;align-items:center;gap:3px}
.contact-line svg{width:6px;height:6px;fill:var(--sky)}
.recipient{position:absolute;left:50px;top:136px;font-size:7.2px;line-height:8.7px;font-style:normal}
.letter-body{position:absolute;left:50px;top:208px;width:398px;font-size:6.5px;line-height:8.7px;text-align:justify}
.letter-body .salutation{font-weight:700;font-size:7px;margin-bottom:8px}
.letter-body p{margin-bottom:8.5px}
.closing{position:absolute;left:50px;top:432px;font-size:7px}
.signature{position:absolute;left:50px;top:445px;width:82px;height:34px;background:linear-gradient(90deg,#eceaf6,#dcd9ef)}
.signer{position:absolute;left:50px;top:489px;font-size:7.2px;line-height:9px}
.signer strong{font-weight:700}
.fax-title{position:absolute;right:50px;top:27px;font-size:50px;font-weight:400;color:var(--navy);line-height:1;letter-spacing:-1px}
.routing{position:absolute;left:50px;top:112px;width:397px;border-collapse:collapse;font-size:6.6px;font-weight:700}
.routing td{border:1px solid var(--rule);height:13px;padding:0 4px}
.routing .label{width:42px}
.routing .value{width:156px}
.flags{position:absolute;left:50px;top:190px;width:397px;height:374px;border:1px solid var(--rule)}
.flag-row{display:flex;height:14px;border-bottom:1px solid var(--rule);background:var(--cell)}
.flag{display:flex;align-items:center;justify-content:center;gap:3px;font-size:6.6px;font-weight:700;border-right:1px solid var(--rule)}
.flag:last-child{border-right:none}
.flag::before{content:"";width:4px;height:4px;border:.7px solid #555;background:#fff}
.comments-label{text-align:center;font-size:6.6px;margin-top:10px}
</style>
</head>
<body>

<section class="sheet letterhead">
  <div class="brand"><span class="brand-dot"></span><span class="brand-name">Corvelles Concept</span></div>
  <div class="contact">
    <div>218 Rue des Tilleuls</div>
    <div>Lavaldière, QC H7X 2K4</div>
    <div class="gap"></div>
    <div class="contact-line"><svg viewBox="0 0 10 10"><path d="M2 0l2 2-1 2 3 3 2-1 2 2-2 2C4 10 0 6 0 2z"/></svg>450.555.0182</div>
    <div class="contact-line"><svg viewBox="0 0 10 10"><path d="M0 2h10v6H0z"/></svg>hello@corvellesconcept.com</div>
    <div class="contact-line"><svg viewBox="0 0 10 10"><circle cx="5" cy="5" r="5"/></svg>www.corvellesconcept.com</div>
  </div>

  <address class="recipient">
    Mr. Gerald Whitcombe<br>President and CEO<br>Norvenna Labs LLC.<br>840 Halden Avenue, Suite 1200<br>New York, NY 10027
  </address>

  <div class="letter-body">
    <div class="salutation">Dear Mr. Whitcombe:</div>
    <p>As Chairperson of the Corporate Conscience Campaign - Helping the Homeless in New York, I am writing this to thank you personally for your company's support in last month's fund-raising effort.</p>
    <p>As I indicated when we spoke on the phone two weeks ago, the campaign was considered a resounding success, raising a total of $1.65 million to-date, significantly exceeding our target of $1 million. Some donations are still trickling in, so we could end up close to a total of $2 million.</p>
    <p>Norvenna Labs was an influential leader throughout the entire three-month campaign. In fact, we couldn't have succeeded without the generous support of your company, both financially, and through your organizational and administrative assistance. Your Team Leader, Marissa Tolland was particularly impressive, going above and beyond what we could have expected of someone performing as a volunteer while continuing on with her day-to-day duties. Please convey my special thanks to Marissa.</p>
    <p>I would also ask you to convey my sincere thanks and congratulations to all of those other people in your company who contributed in any way to the Helping the Homeless Campaign. Please tell them that the sum of their contributions resulted in a major success that they should all be proud of taking part in.</p>
    <p>I believe that the 27 companies that participated in this effort have set a new standard for social responsibility in this community, and have set a powerful example that will inspire other companies and organizations to do the same.</p>
    <p>I look forward to seeing you at the Mayor's special thank you reception next month.</p>
  </div>

  <div class="closing">Yours sincerely,</div>
  <div class="signature" role="img" aria-label="Handwritten signature"></div>
  <div class="signer"><strong>Laurent Desroches</strong><br>Fundraising Chair</div>
</section>

<section class="sheet fax-sheet">
  <div class="brand"><span class="brand-dot"></span><span class="brand-name">Corvelles Concept</span></div>
  <div class="fax-title">FAX</div>

  <table class="routing">
    <tr><td class="label">To:</td><td class="value"></td><td class="label">From:</td><td class="value"></td></tr>
    <tr><td class="label">Fax:</td><td class="value"></td><td class="label">Pages:</td><td class="value"></td></tr>
    <tr><td class="label">Phone:</td><td class="value"></td><td class="label">Date:</td><td class="value"></td></tr>
    <tr><td class="label">Re:</td><td class="value"></td><td class="label">CC:</td><td class="value"></td></tr>
  </table>

  <div class="flags">
    <div class="flag-row">
      <div class="flag" style="width:80px">Urgent</div>
      <div class="flag" style="width:76px">For Review</div>
      <div class="flag" style="width:88px">Please Comment</div>
      <div class="flag" style="width:74px">Please Reply</div>
      <div class="flag" style="flex:1">Confidential</div>
    </div>
    <div class="comments-label">COMMENTS:</div>
  </div>
</section>

</body>
</html>
```